Project, Programme and Portfolio Management Consultant needs a business card

I have recently had someone create a brand guide for me and I wish to have new business cards that incorporate the new brand. I am an independent management consultant working with businesses to improve their ability to deliver their business strategy through selecting the right project, the right people and doing it in the right way. Whilst I am currently working on my own, I am hoping to start to build win business where I need to bring in a team and this branding activity is the start of that process.

Target Market(s)

Medium to large businesses, government departments and defence

Contact Information for Business Card

Name
job title
business name
mobile
email
website
linkedIn profile

Font styles to use
Other font styles liked:
• roboto light

Colors

Designer to choose colors to be used in the design.

Requirements
Must have
• Must use my logo and brand colours (see attached brand guide)

```html
<!DOCTYPE html>
<html lang="en">
<head>
<meta charset="utf-8">
<title>Kelvane Business Card</title>
<link rel="stylesheet" href="https://fonts.googleapis.com/css2?family=Montserrat:wght@400;600&display=swap">
<style>
  :root {
    --backdrop: #161616;
    --card: #242424;
    --card-light: #2c2c2c;
    --gold: #e8b021;
    --white: #f4f4f4;
    --silver: #bdbdbd;
  }
  * { margin: 0; padding: 0; box-sizing: border-box; }
  html, body {
    width: 1200px; height: 900px; overflow: hidden;
    background: var(--backdrop);
    font-family: "Montserrat", sans-serif;
  }
  .canvas { position: relative; width: 1200px; height: 900px; }
  .card {
    position: absolute; left: 250px; width: 700px; height: 400px;
    background: linear-gradient(135deg, var(--card) 0%, var(--card-light) 70%, var(--card) 100%);
  }
  .card-front { top: 40px; }
  .card-back { top: 470px; }

  .front-wordmark {
    position: absolute; left: 0; right: 0; top: 170px;
    text-align: center; color: var(--silver);
    font-size: 40px; font-weight: 400; letter-spacing: 4px;
  }

  .back-wordmark {
    position: absolute; left: 40px; width: 190px; top: 180px;
    text-align: center; color: var(--white);
    font-size: 34px; font-weight: 400; letter-spacing: 2px;
  }
  .divider {
    position: absolute; left: 262px; top: 90px; width: 2px; height: 230px;
    background: var(--gold);
  }
  .details { position: absolute; left: 300px; top: 88px; color: var(--white); }
  .person-name {
    color: var(--gold); font-size: 28px; font-weight: 600; letter-spacing: 2px;
    line-height: 1.1;
  }
  .person-role { font-size: 17px; letter-spacing: 1px; margin-bottom: 16px; }
  .address { font-size: 17px; letter-spacing: 1px; line-height: 1.3; margin-bottom: 14px; }
  .contact-list { list-style: none; }
  .contact-item {
    display: flex; align-items: center; gap: 12px;
    font-size: 17px; letter-spacing: 1px; line-height: 1.45;
  }
  .contact-icon { width: 14px; height: 14px; flex: none; }
</style>
</head>
<body>
<main class="canvas">
  <section class="card card-front">
    <p class="front-wordmark">KELVANE</p>
  </section>

  <section class="card card-back">
    <p class="back-wordmark">KELVANE</p>
    <div class="divider"></div>
    <div class="details">
      <h1 class="person-name">DANIEL HARPER</h1>
      <p class="person-role">Director</p>
      <p class="address">48 Marlow Street<br>Westbury London NW3 4QT</p>
      <ul class="contact-list">
        <li class="contact-item">
          <svg class="contact-icon" viewBox="0 0 14 14"><path d="M3 1 L5 4 L4 5.5 Q5.5 8.5 8.5 10 L10 9 L13 11 L11.5 13 Q5 12 1 3 Z" fill="var(--gold)"/></svg>
          +330 5172-4036
        </li>
        <li class="contact-item">
          <svg class="contact-icon" viewBox="0 0 14 14"><rect x="1" y="3" width="12" height="8" fill="none" stroke="var(--gold)" stroke-width="1.3"/><path d="M1 3 L7 8 L13 3" fill="none" stroke="var(--gold)" stroke-width="1.3"/></svg>
          hello@kelvane.com
        </li>
        <li class="contact-item">
          <svg class="contact-icon" viewBox="0 0 14 14"><circle cx="7" cy="7" r="5.8" fill="none" stroke="var(--gold)" stroke-width="1.2"/><ellipse cx="7" cy="7" rx="2.5" ry="5.8" fill="none" stroke="var(--gold)" stroke-width="1"/><path d="M1.2 7 H12.8" stroke="var(--gold)" stroke-width="1"/></svg>
          www.kelvane.com
        </li>
        <li class="contact-item">
          <svg class="contact-icon" viewBox="0 0 14 14"><rect x="2" y="2" width="10" height="10" fill="var(--gold)"/></svg>
          in/kelvane-4521
        </li>
      </ul>
    </div>
  </section>
</main>
</body>
</html>
```